Create a 3.5" x 8.5" door hanger for a produce delivery company called Uncle Fennel's.

Door hanger should fit the template specifications attached.

Door hanger should include some form of the logo attached.

Door hanger should include the information: "Fresh, local produce, meats, dairy, cheese, and baked goods. Delivered to your door at grocery store prices!"

Door hanger should include the following coupon: "$15.00 OFF! Enter coupon code “doorhanger” during sign up and we’ll waive the enrollment fee and take $5.00 of your first order!"

Door hanger should have the website printed noticeably: UncleFennels.com

Door hanger should include photos of seasonal produce items to the southern US. Some examples include: apples, pumpkins, bell peppers, squashes, eggplant, tomatoes, green beans, carrots, broccoli, greens, sweet potatoes, lettuces, cauliflower, cabbage, radishes.

Industry/Entity Type

Grocery Store

Requirements
Nice to have
• A back side with some or all of the following "About us" information:
• Uncle Fennel's is a farm to fork delivery service, working to bring the entire NC food landscape to your front door! Since 2008 we have been expanding our network of local growers and food artisans, and are happy to be able to offer over 200 food products a week, and we are still growing! Our goal is to greatly improve access to local foods in our community through transparency, communication, affordability, and the convenience of our delivery infrastructure.
• Here are just a few reasons we think you will love working with Uncle Fennel's:
• Wide variety of NC products!
• You will not find a greater variety of NC produce anywhere else, outside of a farmers market.
• Superior freshness, quality, and flavor!
• By working with local growers, products can be fully ripened on the vine, picked and delivered to your door within 48 hours of harvest.
• Affordable!
• We understand that affordability is an important concern for every family. On average our prices are equivalent to grocery store prices when comparing like items (organic to organic, etc.).
• Support your community!
• By purchasing from local farms and food artisans, you are supporting your neighbors and helping to further develop our local food infrastructure.
• Educational!
• Purchasing seasonal products from local farms is a fantastic opportunity to get back to nature and reconnect with what food really is.
• Convenient and easy!
• Not to mention, we deliver to your front door! Easy!

```html
<!DOCTYPE html>
<html lang="en">
<head>
<meta charset="utf-8">
<title>Uncle Fennel's Door Hanger</title>
<link href="https://fonts.googleapis.com/css2?family=Archivo+Black&family=PT+Sans:wght@700&display=swap" rel="stylesheet">
<style>
  :root {
    --ink: #111111;
    --page: #ffffff;
    --hole: #e3edcc;
    --tint-warm: #fde3cf;
    --tint-peach: #fbefe0;
    --tint-green: #e4eedd;
    --tint-violet: #e3e1f3;
  }
  * { box-sizing: border-box; margin: 0; padding: 0; }
  html, body { width: 1200px; height: 1000px; overflow: hidden; background: var(--page); }
  body { position: relative; color: var(--ink); font-family: "PT Sans", Arial, sans-serif; font-weight: 700; }

  .hanger { position: absolute; top: 0; width: 428px; height: 1000px; overflow: hidden; }
  .hanger--front { left: 150px; }
  .hanger--back { left: 622px; }

  .produce-pattern {
    position: absolute; inset: 0;
    background:
      linear-gradient(160deg, var(--tint-warm) 0%, var(--tint-peach) 30%, var(--page) 50%, var(--tint-green) 72%, var(--tint-violet) 100%);
    opacity: .85;
  }

  .knob-hole {
    position: absolute; left: 146px; top: 65px; width: 136px; height: 136px;
    border-radius: 50%; background: var(--hole);
    display: flex; align-items: center; justify-content: center; text-align: center;
    font-family: Arial, Helvetica, sans-serif; font-weight: 700; font-size: 12px; line-height: 15px;
  }

  .content { position: absolute; left: 0; width: 100%; text-align: center; }

  .url { font-family: "Archivo Black", "Arial Black", sans-serif; font-size: 23px; letter-spacing: .5px; }

  .brand-mark { position: absolute; left: 0; top: 270px; width: 428px; height: 200px; }
  .brand-name {
    position: absolute; left: 0; width: 100%; top: 0; text-align: center;
    font-family: "Archivo Black", "Arial Black", sans-serif; font-size: 38px; letter-spacing: 1px;
  }
  .brand-ring {
    position: absolute; left: 129px; top: 48px; width: 150px; height: 150px;
    border: 4px solid var(--ink); border-radius: 50%;
  }

  .front-url-top { top: 472px; }
  .front-copy { top: 502px; font-size: 17.5px; line-height: 22px; }
  .front-copy p { margin-bottom: 20px; }
  .front-copy .lead { margin-bottom: 16px; }
  .offer { top: 840px; }
  .offer-amount { font-size: 25px; line-height: 30px; }
  .offer-terms { font-size: 16.5px; line-height: 22px; }
  .front-url-bottom { top: 940px; }

  .back-url-top { top: 225px; }
  .about { top: 265px; padding: 0 26px; font-size: 10.6px; line-height: 14.1px; }
  .about p { margin-bottom: 11px; }
  .back-url-bottom { top: 944px; }
</style>
</head>
<body>

<section class="hanger hanger--front">
  <div class="produce-pattern" role="img" aria-label="Light line-drawn pattern of seasonal produce and groceries in warm-to-cool pastel tones"></div>
  <div class="knob-hole">DOOR KNOB HOLE<br>IMAGES/TEXT<br>IN THIS<br>AREA<br>WILL BE CUT-OFF</div>

  <div class="brand-mark">
    <div class="brand-ring"></div>
    <div class="brand-name">UNCLE FENNEL'S</div>
  </div>

  <div class="content url front-url-top">UNCLEFENNELS.COM</div>

  <div class="content front-copy">
    <p class="lead">Fresh, local produce, meats, dairy, cheese,<br>and baked goods. Delivered to your door<br>at grocery store prices!</p>
    <p>Wide variety of NC products!</p>
    <p>Superior freshness, quality, and flavor!</p>
    <p>Affordable! &nbsp;&nbsp;Educational!</p>
    <p>Support your community!</p>
    <p>Not to mention,<br>we deliver to your front door!</p>
    <p>Convenient and easy!</p>
  </div>

  <div class="content offer">
    <div class="offer-amount">$15.00 OFF!</div>
    <div class="offer-terms">Enter coupon code “doorhanger” during<br>sign up and we’ll waive the enrollment fee<br>and take $5.00 of your first order!</div>
  </div>

  <div class="content url front-url-bottom">UNCLEFENNELS.COM</div>
</section>

<section class="hanger hanger--back">
  <div class="produce-pattern" role="img" aria-label="Light line-drawn pattern of seasonal produce and groceries in warm-to-cool pastel tones"></div>
  <div class="knob-hole">DOOR KNOB HOLE<br>IMAGES/TEXT<br>IN THIS<br>AREA<br>WILL BE CUT-OFF</div>

  <div class="content url back-url-top">UNCLEFENNELS.COM</div>

  <div class="content about">
    <p>Uncle Fennel's is a farm to fork delivery service, working to bring the entire NC food landscape to your front door! Since 2008 we have been expanding our network of local growers and food artisans, and are happy to be able to offer over 200 food products a week, and we are still growing! Our goal is to greatly improve access to local foods in our community through transparency, communication, affordability, and the convenience of our delivery infrastructure.</p>
    <p>You will not find a greater variety of NC produce anywhere else, outside of a farmers market. We offer all the seasonal staples such as strawberries, blueberries, sweet corn, peaches, summer squashes, etc. as well as lots and lots of specialty produce grown by small local growers that you will never find in a grocery store. We have over 150 different local options every week! By working with local growers, products can be fully ripened on the vine, picked and delivered to your door within 48 hours of harvest. By allowing products to fully ripen, the flavor is far superior and you will recognize an immediate difference between fresh local produce and produce picked unripe and shipped across the country to a grocery store. We publish a market report every week giving you details into how each harvest is going and what you can expect week to week.</p>
    <p>We understand that affordability is an important concern for every family. On average our prices are equivalent to grocery store prices when comparing like items (organic to organic, etc.). We also work hard to communicate how seasons affect pricing, and let you know which items are at their peak season resulting in prices that are often less than the grocery store, and which items are still out of season and more expensive.</p>
    <p>By purchasing from local farms and food artisans, you are supporting your neighbors and helping to further develop our local food infrastructure. In the 6 short years that we have been operating Uncle Fennel's we have seen more and more people getting into farming in our state, more growers expanding into new crops, more growers testing seasonal boundaries and investing in agricultural infrastructure. This is the result of people like you in our community deciding to support local agriculture and providing these growers with a market to sell their goods and expand their operations. This is an extremely positive development for everyone, and everyone should be happy and proud to support local agriculture.</p>
    <p>Purchasing seasonal products from local farms is a fantastic opportunity to get back to nature and reconnect with what food really is. We work very hard to explain how seasons work, when products are available, when they are at their peak, when quality is best, when it might not be so good, and how to use new produce offerings that you may not be familiar with. We offer at least 6 different varieties of eggplant, 8+ varieties of tomatoes, hybrid varieties of greens and cabbage, heirloom cantaloupes, and many other interesting products that have been lost in today's industrial food landscape. Purchasing from local farms gives us the opportunity to get back to our food roots, experiment with new products, some products you'll love, others you may hate, but you will become a much more educated food consumer and will learn a lot about what real food is.</p>
  </div>

  <div class="content url back-url-bottom">UNCLEFENNELS.COM</div>
</section>

</body>
</html>
```